Falzflyer-Design für Softwareprodukte
Zielgruppe
Wir bieten mit unserer Produktlinie Morvane Softwareprodukte für Fluggesellschaften und touristische Unternehmen. Unsere Softwarelösungen sind ein Vertriebssystem für Airlines (Inventory), Prozess-basierte Automatisierungen, Buchungsschnittstellen und Datenanalysen. Weiterhin bieten wir diesen Unternehmen Custom Development und Beratungsdienstleistungen an.
Aufgabenstellung
Wir benötigen einen Falzflyer. Die Maße sind in einem Datenblatt von unserer Druckerei enthalten.
Weiterhin haben wir unser Logo und unserem Color Code hochgeladen. In einem pdf haben wir zusätzlich die Inhalte zusammengefasst (aussen und innen), die im Flyer aufgeführt werden sollen (noch nicht alles ist auf unserer Website verfügbar).
Einige Bilder, die wir auf der Website nutzen bzw. nutzen werden, findet ihr dort auch . Es kann aber gerne anderes Bildmaterial verwendet werden.
Wir überarbeiten gerade unsere Website und nutzen neben den unterschiedlichen Grautönen vorrangig #4b75e5, #00bac9 und folgende Schriftarten: Pragrati Narrow für Überschriften, Open Sans für Texte
Flyer wird ausschließlich in Englisch benötigt.

```html
<!DOCTYPE html>
<html lang="en">
<head>
<meta charset="utf-8">
<title>Aerovant Trifold Flyer</title>
<link href="https://fonts.googleapis.com/css2?family=Open+Sans:ital,wght@0,400;0,600;0,700;1,400;1,700&family=Pragati+Narrow:wght@400;700&display=swap" rel="stylesheet">
<style>
:root{
  --teal-dark:#18a9b9;
  --teal:#1fb5c4;
  --teal-light:#62c5cf;
  --teal-pale:#8fd6dc;
  --white:#ffffff;
  --grey-bg:#ececec;
  --grey-text:#6b6f73;
  --grey-line:#c9ced2;
  --sky-top:#b9c4d2;
  --sky-bottom:#eef1f6;
}
*{box-sizing:border-box;margin:0;padding:0}
html,body{width:1200px;height:2800px;overflow:hidden}
body{background:var(--grey-bg);font-family:"Open Sans",sans-serif;position:relative}
.spread{position:absolute;left:60px;width:1080px;height:770px;display:flex;box-shadow:0 10px 30px rgba(0,0,0,.12);background:var(--white)}
.spread.outer{top:150px}
.spread.inner{top:1080px}
.panel{position:relative;width:360px;height:100%;overflow:hidden}

/* outer: benefits */
.benefits{background:var(--teal-dark);color:var(--white);padding:32px 28px 0}
.panel-title{font-family:"Pragati Narrow",sans-serif;font-weight:700;font-size:34px;text-align:center;line-height:1}
.benefits .panel-title{padding-bottom:14px;border-bottom:1px solid rgba(255,255,255,.6);margin-bottom:12px}
.benefit-list{list-style:none;padding-left:34px}
.benefit{display:flex;align-items:center;gap:14px;padding:12px 0;border-bottom:1px solid rgba(255,255,255,.55);font-family:"Pragati Narrow",sans-serif;font-size:17px;line-height:1.1}
.benefit:last-child{border-bottom:none}
.benefit svg{flex:0 0 44px}
.benefits .plane-photo{position:absolute;left:0;bottom:0;width:100%;height:110px;background:linear-gradient(180deg,rgba(24,169,185,0),rgba(190,225,235,.55))}

/* outer: contact */
.contact{background:var(--teal-light);color:var(--white);text-align:center}
.city-photo{height:210px;background:linear-gradient(180deg,#9db3c9 0%,#c9d3dc 45%,#7f8c94 100%)}
.badge{position:absolute;left:50%;transform:translateX(-50%);width:66px;height:66px;border-radius:50%;background:var(--teal);border:3px solid var(--white);display:flex;align-items:center;justify-content:center}
.contact .badge{top:177px}
.contact .panel-title{margin-top:58px;font-size:32px}
.rule{width:160px;height:1px;background:rgba(255,255,255,.7);margin:16px auto 26px}
.contact-list{list-style:none}
.contact-item{display:flex;flex-direction:column;align-items:center;gap:8px;margin-bottom:20px;font-size:10px;font-weight:600}
.site-url{position:absolute;bottom:22px;left:0;width:100%;font-size:15px;font-weight:700}
.side-mark{position:absolute;left:-26px;top:200px;width:52px;height:52px;border-radius:50%;background:var(--teal-pale)}

/* outer: cover */
.cover{background:var(--white);text-align:center;border-top:8px solid var(--teal-light)}
.brand{font-family:"Open Sans",sans-serif;font-size:40px;font-weight:400;color:var(--grey-text);margin-top:26px;display:flex;align-items:center;justify-content:center;gap:10px}
.brand-dot{width:14px;height:14px;border-radius:50%;background:var(--teal)}
.sky-photo{height:260px;margin-top:18px;background:linear-gradient(180deg,var(--sky-top),var(--sky-bottom))}
.tagline{font-family:"Pragati Narrow",sans-serif;color:var(--grey-text);font-size:20px;line-height:1.05;margin-top:22px;text-transform:uppercase}
.tagline strong{display:block;font-size:30px;color:var(--teal);font-weight:700;margin-top:4px}
.cover-band{position:absolute;left:0;bottom:0;width:100%;height:44px;background:var(--teal-light);color:var(--white);font-size:13px;font-weight:700;display:flex;align-items:center;justify-content:center}

/* inner */
.product{background:var(--white);color:var(--grey-text);text-align:center}
.product-photo{height:150px}
.photo-work{background:linear-gradient(180deg,#b9c4d1,#e3e8ee)}
.photo-map{background:linear-gradient(180deg,#e1e3e6,#f3f4f5)}
.photo-wing{background:linear-gradient(180deg,#8b98a8,#d5dce5)}
.product .badge{top:122px;width:56px;height:56px}
.product-title{font-family:"Open Sans",sans-serif;font-weight:700;font-style:italic;color:var(--teal);font-size:19px;line-height:1.15;text-transform:uppercase;margin-top:46px;padding:0 24px}
.intro{font-size:9.5px;line-height:1.45;padding:0 30px;margin-top:12px;text-align:left}
.key-label{font-size:11px;font-weight:700;text-align:left;padding:0 30px;margin-top:14px;letter-spacing:.03em}
.feature-group{text-align:left;padding:0 30px;margin-top:10px}
.feature-head{font-size:12px;font-weight:700;font-style:italic;color:var(--teal);border-bottom:1px solid var(--teal);padding-bottom:3px;margin-bottom:4px}
.feature-list{list-style:none;font-size:9.5px;line-height:1.5;padding-left:4px}
.feature-list li{display:flex;gap:6px;align-items:flex-start}
.feature-list svg{flex:0 0 9px;margin-top:3px}
.plane-photo-large{position:absolute;left:0;bottom:0;width:100%;height:260px;background:linear-gradient(180deg,rgba(255,255,255,0),#dfe5ee)}
.fold{position:absolute;top:0;width:1px;height:100%;background:rgba(0,0,0,.08)}
</style>
</head>
<body>

<section class="spread outer" aria-label="Flyer outside">
  <div class="panel benefits">
    <h2 class="panel-title">Benefits</h2>
    <ul class="benefit-list">
      <li class="benefit"><svg width="44" height="44" viewBox="0 0 44 44"><circle cx="22" cy="22" r="20" fill="none" stroke="#fff" stroke-width="1.5"/><path d="M14 28h16M16 28v-6M22 28v-10M28 28v-8" stroke="#fff" stroke-width="1.5" fill="none"/></svg>Maximize your<br>revenue</li>
      <li class="benefit"><svg width="44" height="44" viewBox="0 0 44 44"><circle cx="22" cy="22" r="20" fill="none" stroke="#fff" stroke-width="1.5"/><circle cx="16" cy="19" r="3" fill="none" stroke="#fff" stroke-width="1.5"/><circle cx="28" cy="19" r="3" fill="none" stroke="#fff" stroke-width="1.5"/><path d="M16 22v8M28 22v8M16 30h12" stroke="#fff" stroke-width="1.5" fill="none"/></svg>Reduce your<br>distribution cost</li>
      <li class="benefit"><svg width="44" height="44" viewBox="0 0 44 44"><circle cx="22" cy="22" r="20" fill="none" stroke="#fff" stroke-width="1.5"/><path d="M13 29l6-7 5 4 7-9" stroke="#fff" stroke-width="1.5" fill="none"/></svg>Use your competitive<br>advantage</li>
      <li class="benefit"><svg width="44" height="44" viewBox="0 0 44 44"><circle cx="22" cy="22" r="20" fill="none" stroke="#fff" stroke-width="1.5"/><circle cx="22" cy="22" r="7" fill="none" stroke="#fff" stroke-width="1.5"/><circle cx="22" cy="22" r="2" fill="#fff"/></svg>Focus on business<br>processes</li>
      <li class="benefit"><svg width="44" height="44" viewBox="0 0 44 44"><circle cx="22" cy="22" r="20" fill="none" stroke="#fff" stroke-width="1.5"/><rect x="13" y="15" width="18" height="14" fill="none" stroke="#fff" stroke-width="1.5"/><path d="M13 19h18" stroke="#fff" stroke-width="1.5"/></svg>Customize Morvane<br>quick and easy</li>
      <li class="benefit"><svg width="44" height="44" viewBox="0 0 44 44"><circle cx="22" cy="22" r="20" fill="none" stroke="#fff" stroke-width="1.5"/><circle cx="22" cy="22" r="8" fill="none" stroke="#fff" stroke-width="1.5" stroke-dasharray="3 2"/><circle cx="22" cy="22" r="3" fill="none" stroke="#fff" stroke-width="1.5"/></svg>Eliminate<br>complexity</li>
      <li class="benefit"><svg width="44" height="44" viewBox="0 0 44 44"><circle cx="22" cy="22" r="20" fill="none" stroke="#fff" stroke-width="1.5"/><path d="M12 26c4 0 6 3 10 3s6-2 10-5" stroke="#fff" stroke-width="1.5" fill="none"/><circle cx="24" cy="17" r="4" fill="none" stroke="#fff" stroke-width="1.5"/></svg>Pay-as-you-go with<br>no huge up-front<br>costs (SaaS &amp; PaaS)</li>
    </ul>
    <div class="plane-photo" role="img" aria-label="Photo of an airliner fading into the panel"></div>
  </div>

  <div class="panel contact">
    <div class="city-photo" role="img" aria-label="Photo of a city skyline with a TV tower"></div>
    <div class="badge"><svg width="32" height="32" viewBox="0 0 32 32"><path d="M5 8h16v10H12l-4 4v-4H5z" fill="none" stroke="#fff" stroke-width="1.8"/><path d="M23 12h4v10h-3v3l-3-3h-7v-2" fill="none" stroke="#fff" stroke-width="1.8"/></svg></div>
    <h2 class="panel-title">Get in touch<br>with us</h2>
    <div class="rule"></div>
    <ul class="contact-list">
      <li class="contact-item"><svg width="22" height="22" viewBox="0 0 22 22"><circle cx="11" cy="11" r="10" fill="none" stroke="#fff" stroke-width="1.3"/><circle cx="11" cy="9" r="3" fill="none" stroke="#fff" stroke-width="1.3"/><path d="M6 16c1-3 9-3 10 0" stroke="#fff" stroke-width="1.3" fill="none"/></svg>Aerovant GmbH</li>
      <li class="contact-item"><svg width="22" height="22" viewBox="0 0 22 22"><circle cx="11" cy="11" r="10" fill="none" stroke="#fff" stroke-width="1.3"/><path d="M11 17s-4-4-4-7a4 4 0 0 1 8 0c0 3-4 7-4 7z" fill="none" stroke="#fff" stroke-width="1.3"/></svg>Lindenweg 14 | 10115 Berlin</li>
      <li class="contact-item"><svg width="22" height="22" viewBox="0 0 22 22"><circle cx="11" cy="11" r="10" fill="none" stroke="#fff" stroke-width="1.3"/><path d="M7 7l2-1 2 3-1 1a6 6 0 0 0 3 3l1-1 3 2-1 2c-5 0-9-4-9-9z" fill="none" stroke="#fff" stroke-width="1.2"/></svg>Phone: +49 151 24 68 135</li>
      <li class="contact-item"><svg width="22" height="22" viewBox="0 0 22 22"><circle cx="11" cy="11" r="10" fill="none" stroke="#fff" stroke-width="1.3"/><rect x="6" y="7.5" width="10" height="7" fill="none" stroke="#fff" stroke-width="1.2"/><path d="M6 7.5l5 4 5-4" fill="none" stroke="#fff" stroke-width="1.2"/></svg>info@aerovant-air.com</li>
    </ul>
    <p class="site-url">www.aerovant-air.com</p>
  </div>

  <div class="panel cover">
    <p class="brand">Aerovant<span class="brand-dot"></span></p>
    <div class="sky-photo" role="img" aria-label="Photo of an airliner flying through a pale sky"></div>
    <p class="tagline">Unifying touristic<br>and airline business<strong>is our goal</strong></p>
    <p class="tagline">Breaking the<br>technology gap<strong>is our job</strong></p>
    <div class="cover-band">www.aerovant-air.com</div>
  </div>
  <span class="fold" style="left:360px"></span><span class="fold" style="left:720px"></span>
</section>

<section class="spread inner" aria-label="Flyer inside">
  <div class="panel product">
    <div class="product-photo photo-work" role="img" aria-label="Photo of a person working at a window desk"></div>
    <div class="badge"><svg width="28" height="28" viewBox="0 0 28 28"><rect x="6" y="5" width="14" height="18" fill="none" stroke="#fff" stroke-width="1.6"/><path d="M9 10h8M9 14h8M9 18h5" stroke="#fff" stroke-width="1.6"/></svg></div>
    <h2 class="product-title">Aerovant Morvane<br>Inventory</h2>
    <p class="intro">Fully automated inventory and allotment management system for touristic charter and seat only with direct host system integration.</p>
    <p class="key-label">KEY FEATURES:</p>
    <div class="feature-group">
      <h3 class="feature-head">Revenue and Allotment Management</h3>
      <ul class="feature-list">
        <li><svg width="9" height="9" viewBox="0 0 9 9"><circle cx="4.5" cy="4.5" r="4" fill="none" stroke="#6b6f73"/><path d="M2.5 4.6l1.4 1.3 2.6-2.7" fill="none" stroke="#6b6f73"/></svg>Fixed &amp; Pro-rata allotments</li>
        <li><svg width="9" height="9" viewBox="0 0 9 9"><circle cx="4.5" cy="4.5" r="4" fill="none" stroke="#6b6f73"/><path d="M2.5 4.6l1.4 1.3 2.6-2.7" fill="none" stroke="#6b6f73"/></svg>State-of-the-art Pooling solution</li>
        <li><svg width="9" height="9" viewBox="0 0 9 9"><circle cx="4.5" cy="4.5" r="4" fill="none" stroke="#6b6f73"/><path d="M2.5 4.6l1.4 1.3 2.6-2.7" fill="none" stroke="#6b6f73"/></svg>Triangle, Multi-leg &amp; Hub Management</li>
      </ul>
    </div>
    <div class="feature-group">
      <h3 class="feature-head">Seat only and Ancillary Management</h3>
      <ul class="feature-list">
        <li><svg width="9" height="9" viewBox="0 0 9 9"><circle cx="4.5" cy="4.5" r="4" fill="none" stroke="#6b6f73"/><path d="M2.5 4.6l1.4 1.3 2.6-2.7" fill="none" stroke="#6b6f73"/></svg>Seat map &amp; Ancillary Management</li>
        <li><svg width="9" height="9" viewBox="0 0 9 9"><circle cx="4.5" cy="4.5" r="4" fill="none" stroke="#6b6f73"/><path d="M2.5 4.6l1.4 1.3 2.6-2.7" fill="none" stroke="#6b6f73"/></svg>Waitlist Management</li>
        <li><svg width="9" height="9" viewBox="0 0 9 9"><circle cx="4.5" cy="4.5" r="4" fill="none" stroke="#6b6f73"/><path d="M2.5 4.6l1.4 1.3 2.6-2.7" fill="none" stroke="#6b6f73"/></svg>Sales Channel Management with focus on touristic channels</li>
      </ul>
    </div>
    <div class="feature-group">
      <h3 class="feature-head">Data Processing and Api Management</h3>
      <ul class="feature-list">
        <li><svg width="9" height="9" viewBox="0 0 9 9"><circle cx="4.5" cy="4.5" r="4" fill="none" stroke="#6b6f73"/><path d="M2.5 4.6l1.4 1.3 2.6-2.7" fill="none" stroke="#6b6f73"/></svg>Passenger name list processing (PNL/ADL)</li>
        <li><svg width="9" height="9" viewBox="0 0 9 9"><circle cx="4.5" cy="4.5" r="4" fill="none" stroke="#6b6f73"/><path d="M2.5 4.6l1.4 1.3 2.6-2.7" fill="none" stroke="#6b6f73"/></svg>PSS integration (Orbiqa, Travelink, etc.)</li>
        <li><svg width="9" height="9" viewBox="0 0 9 9"><circle cx="4.5" cy="4.5" r="4" fill="none" stroke="#6b6f73"/><path d="M2.5 4.6l1.4 1.3 2.6-2.7" fill="none" stroke="#6b6f73"/></svg>Post Flight Processing</li>
      </ul>
    </div>
  </div>

  <div class="panel product">
    <div class="product-photo photo-map" role="img" aria-label="Faint world map with a boarding pass and magnifier"></div>
    <div class="badge"><svg width="28" height="28" viewBox="0 0 28 28"><circle cx="14" cy="14" r="5" fill="none" stroke="#fff" stroke-width="1.6"/><circle cx="14" cy="14" r="9" fill="none" stroke="#fff" stroke-width="1.6" stroke-dasharray="3 2.5"/></svg></div>
    <h2 class="product-title">Aerovant Morvane<br>Automate</h2>
    <p class="intro">Aerovant Morvane Automate enables the complete automation of existing and new back-office processes, resulting in increasing revenue as well as significant cost and time savings.</p>
    <p class="key-label">KEY FEATURES:</p>
    <div class="feature-group">
      <ul class="feature-list">
        <li><svg width="9" height="9" viewBox="0 0 9 9"><circle cx="4.5" cy="4.5" r="4" fill="none" stroke="#6b6f73"/><path d="M2.5 4.6l1.4 1.3 2.6-2.7" fill="none" stroke="#6b6f73"/></svg>Rule engine - based Revenue integrity</li>
        <li><svg width="9" height="9" viewBox="0 0 9 9"><circle cx="4.5" cy="4.5" r="4" fill="none" stroke="#6b6f73"/><path d="M2.5 4.6l1.4 1.3 2.6-2.7" fill="none" stroke="#6b6f73"/></svg>Back-office automation with Queue Management, Ticketing, Reissue &amp; Revalidation</li>
        <li><svg width="9" height="9" viewBox="0 0 9 9"><circle cx="4.5" cy="4.5" r="4" fill="none" stroke="#6b6f73"/><path d="M2.5 4.6l1.4 1.3 2.6-2.7" fill="none" stroke="#6b6f73"/></svg>Mass rebooking &amp; PNR updates &amp; FTC-handling</li>
        <li><svg width="9" height="9" viewBox="0 0 9 9"><circle cx="4.5" cy="4.5" r="4" fill="none" stroke="#6b6f73"/><path d="M2.5 4.6l1.4 1.3 2.6-2.7" fill="none" stroke="#6b6f73"/></svg>Customized communication &amp; invoicing</li>
        <li><svg width="9" height="9" viewBox="0 0 9 9"><circle cx="4.5" cy="4.5" r="4" fill="none" stroke="#6b6f73"/><path d="M2.5 4.6l1.4 1.3 2.6-2.7" fill="none" stroke="#6b6f73"/></svg>Loyalty Program &amp; Branded Fare Management in PSS</li>
        <li><svg width="9" height="9" viewBox="0 0 9 9"><circle cx="4.5" cy="4.5" r="4" fill="none" stroke="#6b6f73"/><path d="M2.5 4.6l1.4 1.3 2.6-2.7" fill="none" stroke="#6b6f73"/></svg>Sales channel synchronization</li>
      </ul>
    </div>
    <div class="plane-photo-large" role="img" aria-label="Photo of an airliner climbing through soft clouds"></div>
  </div>

  <div class="panel product">
    <div class="product-photo photo-wing" role="img" aria-label="Photo of an aircraft wing above the clouds"></div>
    <div class="badge"><svg width="28" height="28" viewBox="0 0 28 28"><path d="M6 22h16M8 22v-6M12 22v-9M16 22v-7M20 22v-11" stroke="#fff" stroke-width="1.6" fill="none"/></svg></div>
    <h2 class="product-title">Aerovant Custom<br>Development</h2>
    <p class="intro">We provide custom development based on modern technology and deep airplane and touristic knowledge.</p>
    <p class="intro">As experienced Airline-IT developers we implement your requirements fast and reliable.</p>
    <div class="plane-photo-large" role="img" aria-label="Photo of an airliner flying above a sea of clouds"></div>
  </div>
  <span class="fold" style="left:360px"></span><span class="fold" style="left:720px"></span>
</section>

</body>
</html>
```